Marbeck Partners Exit Plan business consultant web site

This website is for a consulting business that helps other businesses with exit plans. Essentially, assists them with the sale of their business. This website should be very professional, almost with a wall street look. I would like a very attractive image on the homepage. Perhaps something that denotes success. Perhaps a picture of palm trees and a beach? I will leave it to you for interpretation.

Across the screen I would like the words "Does your business have an exit plan?"

Below that it should read the following:
Let us help you with a completely impartial, no obligation assessment (button with link to the contact page)

Also, please use logo in a prominent place on the website so it's easily seen.

Target Market(s)

Males 40+

Coding

Coded - Design and coding required

Number of Pages Required

5+ page

Colors

Designer to choose colors to be used in the design.

Requirements
Must have
• The tabs for the homepage on the top should be:
• 1. About us
• 2. Services
• 3. Industries
• 4. Our success
• 5. Contact
Nice to have
• Clean, professional image.
• Please put FB, Twitter, Linked In - logos at bottom.
• Here are two examples of a website to give you an idea:
• https://blog.trevanquill.com/library/why-every-business-owner-should-have-an-exit-plan
Should not have
• nothing whimsical or cartoon like

```html
<!DOCTYPE html>
<html lang="en">
<head>
<meta charset="utf-8">
<title>Marbeck Partners – Exit Planning Consultants</title>
<link rel="stylesheet" href="https://fonts.googleapis.com/css2?family=Poppins:ital,wght@0,300;0,400;0,500;0,600;0,700;1,400&display=swap">
<style>
:root{
  --ink:#111111;
  --text:#333333;
  --muted:#555555;
  --white:#ffffff;
  --nav-active:#333333;
  --card-grey:#666666;
  --section-grey:#f7f7f7;
  --testi-grey:#f3f3f3;
  --footer-dark:#232323;
  --footer-mid:#4b4b4b;
}
*{box-sizing:border-box;margin:0;padding:0}
html,body{width:1200px;height:3703px;overflow:hidden}
body{position:relative;font-family:"Poppins",sans-serif;color:var(--text);background:var(--white)}
.abs{position:absolute}
a{color:inherit;text-decoration:none}

/* header */
.header{top:0;left:0;width:1200px;height:233px;background:var(--white)}
.contact-chip{top:56px;display:flex;align-items:center;gap:16px}
.chip-icon{width:48px;height:48px;border-radius:50%;background:var(--ink);display:flex;align-items:center;justify-content:center}
.chip-label{font-size:16px;font-weight:600;color:var(--ink);line-height:1.5}
.chip-value{font-size:17px;font-weight:600;color:var(--ink)}
.brand{top:40px;left:0;width:1200px;display:flex;flex-direction:column;align-items:center;gap:14px}
.brand-square{width:58px;height:58px;border:3px solid var(--ink)}
.brand-name{font-size:28px;font-weight:400;letter-spacing:2px;color:var(--ink);text-transform:uppercase}
.nav{top:168px;left:112px;width:976px;height:65px;border-top:2px solid var(--ink);display:flex}
.nav a{display:flex;align-items:center;height:63px;font-size:16px;font-weight:500;color:var(--ink);padding:0 0 0 0}
.nav .item{margin-right:62px}
.nav .active{background:var(--nav-active);color:var(--white);padding:0 36px;margin:0 26px 0 50px}

/* hero */
.hero{top:233px;left:0;width:1200px;height:533px;background:linear-gradient(100deg,#2a231d 0%,#3f342a 40%,#5a4d42 70%,#6c6359 100%)}
.hero h1{top:115px;left:112px;font-size:46px;font-weight:600;color:var(--white);line-height:1.2}
.hero .sub{top:172px;left:112px;font-size:38px;font-weight:300;color:var(--white)}
.hero p{top:242px;left:112px;font-size:19px;font-weight:500;color:var(--white);line-height:1.65}
.btn{display:flex;align-items:center;justify-content:center;font-size:16px;font-weight:600;text-transform:uppercase}
.btn-white{background:var(--white);color:var(--ink)}
.btn-black{background:var(--ink);color:var(--white)}
.hero .btn{top:333px;left:112px;width:130px;height:58px}

/* about */
.eyebrow{font-size:26px;font-weight:300;color:var(--ink)}
.title{font-size:42px;font-weight:600;color:var(--ink);line-height:1.2}
.body-copy{font-size:13.6px;line-height:24px;color:var(--muted);text-align:justify}
.about-eyebrow{top:880px;left:112px}
.about-title{top:915px;left:112px}
.about-copy{top:983px;left:112px;width:549px}
.about-copy p+p{margin-top:10px}
.about-btn{top:1236px;left:112px;width:130px;height:57px}
.about-media{top:866px;left:713px;width:375px;height:450px;border:3px solid var(--card-grey)}
.about-media .photo{position:absolute;inset:6px;background:linear-gradient(135deg,#5d5a57,#7b7670 50%,#4a4744)}
.about-media .frame{position:absolute;inset:14px;border:6px solid var(--white)}

/* services */
.services{top:1420px;left:0;width:1200px;height:715px;background:var(--section-grey)}
.center{left:0;width:1200px;text-align:center}
.svc-eyebrow{top:56px}
.svc-title{top:92px}
.svc-desc{top:160px;left:150px;width:900px;text-align:center;font-size:13.6px;line-height:24px;color:var(--muted)}
.card{top:248px;width:302px;height:365px;background:var(--card-grey);color:var(--white);text-align:center}
.card.featured{background:var(--ink)}
.card .inner{position:absolute;inset:9px;border:5px solid var(--white)}
.card svg{position:absolute;top:42px;left:121px}
.card h3{position:absolute;top:140px;left:0;width:100%;font-size:23px;font-weight:600}
.card p{position:absolute;top:184px;left:30px;width:242px;font-size:14px;line-height:22px}
.card .btn{position:absolute;top:267px;left:99px;width:104px;height:53px;font-size:14px;font-weight:500}

/* success */
.success-media{top:2135px;left:0;width:520px;height:592px;background:radial-gradient(ellipse at 40% 45%,#e9f4f8 0%,#f2f8fa 45%,#ffffff 75%)}
.success-media .figure{position:absolute;left:65px;top:55px;width:330px;height:537px;border-radius:150px 150px 0 0;background:linear-gradient(180deg,#d9b48a 0%,#c9a07a 25%,#2a2a2e 45%,#1c1c20 100%)}
.success-eyebrow{top:2235px;left:538px;font-size:24px}
.success-title{top:2270px;left:538px}
.success-copy{top:2338px;left:538px;width:550px}
.success-copy p+p{margin-top:10px}
.success-btn{top:2588px;left:538px;width:130px;height:57px}

/* testimonials */
.testimonials{top:2727px;left:0;width:1200px;height:620px;background:var(--testi-grey)}
.t-eyebrow{top:62px}
.t-title{top:98px}
.quote-mark{top:176px;left:547px;width:106px;height:106px;border-radius:50%;background:var(--footer-dark);display:flex;align-items:center;justify-content:center}
.quote-text{top:308px;left:120px;width:960px;text-align:center;font-size:14.5px;font-style:italic;line-height:30px;color:var(--text)}
.quote-name{top:390px;font-size:14.5px;color:var(--text)}
.dots{top:447px;left:552px;display:flex;gap:5px}
.dots span{width:16px;height:16px;border-radius:50%;border:1.5px solid var(--text)}
.dots span.on{background:var(--text)}

/* footer */
.footer-shape{top:3250px;left:0}
.footer-title{top:3362px;left:112px;font-size:30px;font-weight:600;color:var(--white)}
.f-item{left:112px;display:flex;gap:14px;color:var(--white)}
.f-pin{width:38px;height:38px;border-radius:50%;border:2px solid var(--white);display:flex;align-items:center;justify-content:center;flex:none;margin-top:10px}
.f-item h4{font-size:19px;font-weight:600;line-height:1.5}
.f-item p{font-size:15px;line-height:22px}
.f-brand{top:3390px;left:669px;width:420px;display:flex;flex-direction:column;align-items:center;gap:22px}
.f-brand .brand-square{border-color:var(--white);width:96px;height:96px}
.f-brand .brand-name{color:var(--white);font-size:34px}
.f-rule{top:3616px;left:669px;width:420px;height:2px;background:var(--white)}
.copyright{top:3645px;left:665px;font-size:15px;font-weight:500;color:var(--white)}
</style>
</head>
<body>

<header class="abs header">
  <div class="abs contact-chip" style="left:112px">
    <div class="chip-icon">
      <svg width="20" height="16" viewBox="0 0 20 16" fill="none" stroke="#fff" stroke-width="2"><rect x="1" y="1" width="18" height="14" rx="2"/><path d="M1 3l9 6 9-6"/></svg>
    </div>
    <div><div class="chip-label">EMAIL:</div><div class="chip-value">info@marbeckpartners.com</div></div>
  </div>
  <div class="abs brand">
    <div class="brand-square"></div>
    <div class="brand-name">Marbeck Partners</div>
  </div>
  <div class="abs contact-chip" style="left:906px">
    <div class="chip-icon">
      <svg width="18" height="18" viewBox="0 0 24 24" fill="#fff"><path d="M6.6 10.8a15.1 15.1 0 006.6 6.6l2.2-2.2c.3-.3.7-.4 1-.2 1.1.4 2.3.6 3.6.6.6 0 1 .4 1 1V20c0 .6-.4 1-1 1A17 17 0 013 4c0-.6.4-1 1-1h3.5c.6 0 1 .4 1 1 0 1.3.2 2.5.6 3.6.1.3 0 .7-.2 1z"/></svg>
    </div>
    <div><div class="chip-label">PHONE:</div><div class="chip-value">+1 617 555 0148</div></div>
  </div>
  <nav class="abs nav">
    <a class="active" href="#">HOME</a>
    <a class="item" href="#">ABOUT US</a>
    <a class="item" href="#">SERVICES</a>
    <a class="item" href="#">INDUSTRIES</a>
    <a class="item" href="#">OUR SUCCESS</a>
    <a class="item" href="#">CONTACT</a>
  </nav>
</header>

<section class="abs hero" role="img" aria-label="Overhead photo of a desk with laptop, coffee cup, calendar and business papers">
  <h1 class="abs">Does Your Business</h1>
  <div class="abs sub">Have An Exit Plan</div>
  <p class="abs">Let us help you with a completely impartial,<br>no obligation assessment</p>
  <a class="abs btn btn-white" href="#">Contact Us</a>
</section>

<div class="abs eyebrow about-eyebrow">About</div>
<h2 class="abs title about-title">Marbeck Partners</h2>
<div class="abs body-copy about-copy">
  <p>Nam libero tempore, cum soluta nobis est eligendi optio cumque nihil impedit quo minus id quod maxime placeat facere possimus, omnis voluptas assumenda est, omnis dolor repellendus. Temporibus autem quibusdam et aut officiis debitis aut rerum necessitatibus saepe eveniet ut et voluptates repudiandae sint et molestiae non recusandae. Itaque earum rerum hic tenetur a sapiente delectus, ut aut reiciendis</p>
  <p>Temporibus autem quibusdam et aut officiis debitis aut rerum necessitatibus saepe eveniet ut et voluptates repudiandae sint et molestiae non recusandae. Itaque earum rerum hic tenetur a sapiente delectus,.</p>
</div>
<a class="abs btn btn-black about-btn" href="#">Contact Us</a>
<div class="abs about-media">
  <div class="photo" role="img" aria-label="Photo of a team meeting around a conference table"></div>
  <div class="frame"></div>
</div>

<section class="abs services">
  <div class="abs center eyebrow svc-eyebrow">Our</div>
  <h2 class="abs center title svc-title">Group Services</h2>
  <p class="abs svc-desc">Nam libero tempore, cum soluta nobis est eligendi optio cumque nihil impedit quo minus id quod maxime placeat facere possimus, omnis voluptas assumenda est, omnis dolor repellendus.</p>

  <div class="abs card" style="left:112px">
    <div class="inner"></div>
    <svg width="60" height="60" viewBox="0 0 60 60" fill="none" stroke="#fff" stroke-width="2.5"><rect x="10" y="4" width="36" height="50"/><path d="M46 54h6V44h-6"/><path d="M16 14h5v5h-5zM16 26h5v5h-5zM16 38h5v5h-5zM26 16h14M26 28h14M26 40h14"/></svg>
    <h3>Friendly Support</h3>
    <p>Lorem ipsum dolor sit amet, consectetur adipiscing elit, sed do eiusmod tempor.</p>
    <a class="btn btn-white" href="#">Read More</a>
  </div>
  <div class="abs card featured" style="left:449px">
    <div class="inner"></div>
    <svg width="60" height="60" viewBox="0 0 60 60" fill="none" stroke="#fff" stroke-width="2.5"><circle cx="30" cy="30" r="11"/><circle cx="30" cy="27" r="3" fill="#fff"/><circle cx="30" cy="6" r="4"/><circle cx="30" cy="54" r="4"/><circle cx="6" cy="30" r="4"/><circle cx="54" cy="30" r="4"/><circle cx="13" cy="13" r="4"/><circle cx="47" cy="13" r="4"/><circle cx="13" cy="47" r="4"/><circle cx="47" cy="47" r="4"/><path d="M30 10v9M30 41v9M10 30h9M41 30h9M16 16l6 6M44 16l-6 6M16 44l6-6M44 44l-6-6"/></svg>
    <h3>Best Business Plan</h3>
    <p>Lorem ipsum dolor sit amet, consectetur adipiscing elit, sed do eiusmod tempor.</p>
    <a class="btn btn-white" href="#">Read More</a>
  </div>
  <div class="abs card" style="left:786px">
    <div class="inner"></div>
    <svg width="60" height="60" viewBox="0 0 60 60" fill="none" stroke="#fff" stroke-width="2.5"><rect x="18" y="4" width="24" height="16" rx="2"/><path d="M23 10h14M23 15h10M30 20v10M10 30h40M10 30v10M30 30v10M50 30v10"/><rect x="4" y="40" width="12" height="12" rx="2"/><rect x="24" y="40" width="12" height="12" rx="2"/><rect x="44" y="40" width="12" height="12" rx="2"/></svg>
    <h3>Increase Business</h3>
    <p>Lorem ipsum dolor sit amet, consectetur adipiscing elit, sed do eiusmod tempor.</p>
    <a class="btn btn-white" href="#">Read More</a>
  </div>
</section>

<div class="abs success-media">
  <div class="figure" role="img" aria-label="Photo of a smiling businesswoman in a dark suit writing on a clipboard"></div>
</div>
<div class="abs eyebrow success-eyebrow">Marbeck Partners</div>
<h2 class="abs title success-title">Our Success</h2>
<div class="abs body-copy success-copy">
  <p>Nam libero tempore, cum soluta nobis est eligendi optio cumque nihil impedit quo minus id quod maxime placeat facere possimus, omnis voluptas assumenda est, omnis dolor repellendus. Temporibus autem quibusdam et aut officiis debitis aut rerum necessitatibus saepe eveniet ut et voluptates repudiandae sint et molestiae non recusandae. Itaque earum rerum hic tenetur a sapiente delectus, ut aut reiciendis</p>
  <p>Temporibus autem quibusdam et aut officiis debitis aut rerum necessitatibus saepe eveniet ut et voluptates repudiandae sint et molestiae non recusandae. Itaque earum rerum hic tenetur a sapiente delectus,.</p>
</div>
<a class="abs btn btn-black success-btn" href="#">Contact Us</a>

<section class="abs testimonials">
  <div class="abs center eyebrow t-eyebrow">Our</div>
  <h2 class="abs center title t-title">Testimonials</h2>
  <div class="abs quote-mark">
    <svg width="48" height="38" viewBox="0 0 48 38" fill="#fff"><path d="M0 38V22C0 10 6 3 18 0l2 6c-6 2-9 6-9 12h8v20zM27 38V22C27 10 33 3 45 0l2 6c-6 2-9 6-9 12h8v20z"/></svg>
  </div>
  <p class="abs quote-text">Sed ut perspiciatis unde omnis iste natus error sit voluptatem accusantium doloremque laudantium, totam rem aperiam, eaque ipsa quae ab illo inventore veritatis et quasi architecto beatae vitae dicta sunt explicabo.</p>
  <div class="abs center quote-name">- Daniel Hartwell</div>
  <div class="abs dots"><span class="on"></span><span></span><span></span><span></span><span></span></div>
</section>

<svg class="abs footer-shape" width="1200" height="453" viewBox="0 0 1200 453">
  <path d="M0 95 Q300 10 600 0 L600 453 L0 453Z" fill="var(--footer-dark)"/>
  <path d="M600 0 Q900 10 1200 95 L1200 453 L600 453Z" fill="var(--footer-mid)"/>
</svg>

<footer>
  <h2 class="abs footer-title">Contact Us</h2>
  <div class="abs f-item" style="top:3428px">
    <div class="f-pin"><svg width="14" height="18" viewBox="0 0 14 18" fill="#fff"><path d="M7 0a7 7 0 00-7 7c0 5 7 11 7 11s7-6 7-11a7 7 0 00-7-7zm0 9.5A2.5 2.5 0 117 4.5a2.5 2.5 0 010 5z"/></svg></div>
    <div><h4>Address:</h4><p>88 Carrow Lane,<br>Suite 210, Ashford Hills, MA 01790</p></div>
  </div>
  <div class="abs f-item" style="top:3522px">
    <div class="f-pin"><svg width="14" height="18" viewBox="0 0 14 18" fill="#fff"><path d="M7 0a7 7 0 00-7 7c0 5 7 11 7 11s7-6 7-11a7 7 0 00-7-7zm0 9.5A2.5 2.5 0 117 4.5a2.5 2.5 0 010 5z"/></svg></div>
    <div><h4>Phone:</h4><p>+1 617 555 0148</p></div>
  </div>
  <div class="abs f-item" style="top:3600px">
    <div class="f-pin"><svg width="14" height="18" viewBox="0 0 14 18" fill="#fff"><path d="M7 0a7 7 0 00-7 7c0 5 7 11 7 11s7-6 7-11a7 7 0 00-7-7zm0 9.5A2.5 2.5 0 117 4.5a2.5 2.5 0 010 5z"/></svg></div>
    <div><h4>Email:</h4><p>info@marbeckpartners.com</p></div>
  </div>
  <div class="abs f-brand">
    <div class="brand-square"></div>
    <div class="brand-name">Marbeck Partners</div>
  </div>
  <div class="abs f-rule"></div>
  <div class="abs copyright">Copyrights @ 2020 Marbeck Partners. All Rights Reserved.</div>
</footer>

</body>
</html>
```